KEV Formula Body Wash & Shampoo

Label design for an Activated charcoal body wash and shampoo for first responders after fires. Product removes soot and smoke smell. Deep cleansing. Red and black tones in label. Product is deep black and bottle transparent. Label is wrapped around bottle and can be with transparent or coloured background. Bottle diameter is 19cm and height is 17cm.

Target Market(s)

Product will be used by Firefighters, first responders, outdoor/nature active and grill enthusiasts.

Industry/Entity Type

Health and hygiene

Colors
EB3D1F
EC4F4E
F09395
F8D3D4
FCEDEE

Requirements
Must have
• Serious design. Design that fits for 250 and 500ml bottles. Place for ingredients and contact info at the back of the bottle..
Nice to have
• Attractive clean design, attached logo. Logo can be on front or back. "medical" or health associations would be good.
Should not have
• Multi color, pictures. Playfulness.

```html
<!DOCTYPE html>
<html lang="en">
<head>
<meta charset="utf-8">
<title>KEV Formula Body Wash &amp; Shampoo Label</title>
<link href="https://fonts.googleapis.com/css2?family=PT+Sans:ital,wght@0,400;0,700;1,400;1,700&display=swap" rel="stylesheet">
<style>
  :root {
    --red: #d0202a;
    --red-top: #e23038;
    --red-bottom: #c2161e;
    --white: #ffffff;
    --page: #ececec;
    --page-light: #fafafa;
    --charcoal-dark: #2a2a2a;
    --charcoal-mid: #555555;
    --charcoal-light: #8a8a8a;
  }
  html, body {
    margin: 0;
    padding: 0;
    width: 1200px;
    height: 905px;
    overflow: hidden;
    background: radial-gradient(ellipse at 50% 35%, var(--page-light) 0%, var(--page) 70%);
    font-family: "PT Sans", sans-serif;
  }
  .canvas {
    position: relative;
    width: 1200px;
    height: 905px;
  }
  .label {
    position: absolute;
    left: 395px;
    top: 42px;
    width: 410px;
    height: 820px;
  }
  .label text { font-family: "PT Sans", sans-serif; }
  .brand-name { font-weight: 700; font-size: 24px; fill: var(--red); }
  .category { font-weight: 700; font-size: 9px; fill: var(--red); letter-spacing: 0.5px; }
  .product-title { font-weight: 700; font-size: 16.5px; fill: var(--red); }
  .tagline { font-style: italic; font-weight: 700; font-size: 8px; fill: var(--white); }
  .ingredient-note { font-style: italic; font-weight: 700; font-size: 7px; fill: var(--white); }
  .approved-label { font-weight: 700; font-size: 5px; fill: var(--white); }
  .partner-name { font-weight: 700; font-size: 5.5px; fill: var(--white); }
  .volume { font-size: 7px; fill: var(--white); }
</style>
</head>
<body>
<main class="canvas">
  <svg class="label" viewBox="0 0 188 376" xmlns="http://www.w3.org/2000/svg" aria-label="KEV Formula decontamination body wash and shampoo label">
    <defs>
      <clipPath id="label-shape">
        <path d="M0,368 V92 A94,92 0 0 1 188,92 V368 Q188,376 180,376 H8 Q0,376 0,368 Z"/>
      </clipPath>
      <linearGradient id="red-field" x1="0" y1="0" x2="0" y2="1">
        <stop offset="0" stop-color="var(--red-top)"/>
        <stop offset="1" stop-color="var(--red-bottom)"/>
      </linearGradient>
      <linearGradient id="charcoal-fill" x1="0" y1="0" x2="1" y2="1">
        <stop offset="0" stop-color="var(--charcoal-dark)"/>
        <stop offset="0.6" stop-color="var(--charcoal-mid)"/>
        <stop offset="1" stop-color="var(--charcoal-light)"/>
      </linearGradient>
    </defs>

    <g clip-path="url(#label-shape)">
      <rect class="label-base" x="0" y="0" width="188" height="376" fill="var(--white)"/>
      <path class="red-field" d="M0,178 Q94,214 188,178 V376 H0 Z" fill="url(#red-field)"/>
      <path class="divider-line" d="M0,184 Q94,216 188,184" fill="none" stroke="var(--white)" stroke-width="2"/>
      <path class="product-photo" role="img" aria-label="Photo of activated charcoal pieces, charcoal powder and a green bamboo leaf"
            d="M112,236 Q142,196 188,190 V272 Q150,278 122,268 Q106,256 112,236 Z" fill="url(#charcoal-fill)"/>
    </g>

    <path class="label-outline" d="M0,368 V92 A94,92 0 0 1 188,92 V368 Q188,376 180,376 H8 Q0,376 0,368 Z"
          fill="none" stroke="var(--red)" stroke-width="2"/>

    <text class="brand-name" x="94" y="66" text-anchor="middle">KEV Formula</text>
    <text class="category" x="94" y="96" text-anchor="middle">DECONTAMINATION</text>

    <text class="product-title" x="94" y="142" text-anchor="middle">BODY WASH</text>
    <text class="product-title" x="94" y="164" text-anchor="middle">&amp; SHAMPOO</text>

    <text class="tagline" x="10" y="226">Your tagline</text>
    <text class="tagline" x="10" y="236">here!</text>
    <path class="drop" d="M94,222 C90,236 84,244 84,251 A10,10 0 0 0 104,251 C104,244 98,236 94,222 Z" fill="var(--white)"/>

    <text class="ingredient-note" x="112" y="284">with</text>
    <text class="ingredient-note" x="96" y="293">Activated Charcoal</text>

    <text class="approved-label" x="94" y="320" text-anchor="middle">APPROVED BY:</text>
    <circle class="partner-mark" cx="94" cy="334" r="8" fill="var(--white)"/>
    <text class="partner-name" x="94" y="353" text-anchor="middle">SAFE RESPONDERS</text>

    <text class="volume" x="178" y="366" text-anchor="end">500ml</text>
  </svg>
</main>
</body>
</html>
```